Business Card for Bramble Gear

Target Market(s)

Mining, fleet, 4wd industry

Industry/Entity Type

Business

Requirements
Must have
• Front of card
Logo of Bramble Gear, the Nut preferrably top right corner and wording which says
"The Classic Kordo Bolt Products along bottom right hand corner
Use of the orange logo.
Back of card down left side to include (bullet points )
. Canvas Seat Covers
. Hi - Vis Flags
. Canvas or PVC designs by request.
back of card down right side
Danielle Rowbeck
Ph 02 49315728
E ; admin@bramblegear.com.au
W: www.bramblegear.com.au
Nice to have
• other designs can also be submitted as we require additional cards.

```html
<!DOCTYPE html>
<html lang="en">
<head>
<meta charset="utf-8">
<title>Bramble Gear – Business Card</title>
<link rel="stylesheet" href="https://fonts.googleapis.com/css2?family=Open+Sans:wght@400;600;800&family=Lora:ital,wght@1,400&display=swap">
<style>
  :root {
    --orange: #f28a12;
    --charcoal: #4a4a4a;
    --charcoal-dark: #3a3a3a;
    --card-white: #f3f3f3;
    --ink: #555555;
    --page: #e6e2dc;
    --white: #ffffff;
  }
  * { margin: 0; padding: 0; box-sizing: border-box; }
  html, body {
    width: 1200px;
    height: 900px;
    overflow: hidden;
    background: var(--page);
  }
  .sheet {
    width: 1200px;
    height: 900px;
    display: flex;
    flex-direction: column;
    align-items: center;
    justify-content: center;
    gap: 40px;
  }
  .card {
    width: 700px;
    height: 400px;
    display: block;
    box-shadow: 0 6px 18px rgba(0,0,0,0.18);
  }
  .brand-name {
    font-family: "Open Sans", sans-serif;
    font-weight: 800;
    font-size: 34px;
    letter-spacing: 1px;
    fill: var(--white);
  }
  .service-label {
    font-family: "Lora", serif;
    font-style: italic;
    font-size: 20px;
    fill: var(--white);
  }
  .holder-name {
    font-family: "Lora", serif;
    font-style: italic;
    font-size: 27px;
    fill: var(--ink);
  }
  .contact-line {
    font-family: "Lora", serif;
    font-style: italic;
    font-size: 17px;
    fill: var(--ink);
  }
  .tagline {
    font-family: "Open Sans", sans-serif;
    font-weight: 600;
    font-size: 19px;
    fill: var(--white);
  }
  .icon-ring { fill: none; stroke: var(--orange); stroke-width: 2; }
  .icon-glyph { fill: var(--orange); }
</style>
</head>
<body>
<main class="sheet">

  <!-- Front of card -->
  <svg class="card card-front" viewBox="0 0 700 400" xmlns="http://www.w3.org/2000/svg">
    <rect width="700" height="400" fill="var(--card-white)"/>
    <path class="top-sweep-line" d="M0 92 C260 80 500 100 700 150 V136 C500 88 260 68 0 80 Z" fill="var(--charcoal)"/>
    <path class="top-band" d="M0 0 H700 V128 C500 80 260 64 0 74 Z" fill="var(--orange)"/>
    <text class="brand-name" x="36" y="55">BRAMBLE GEAR</text>

    <circle class="emblem-shadow" cx="578" cy="214" r="58" fill="var(--charcoal-dark)"/>
    <circle class="emblem" cx="588" cy="206" r="56" fill="var(--orange)" role="img" aria-label="Kordo Bolt mascot illustration"/>

    <path class="tagline-tab" d="M296 288 H700 V332 H296 Q290 332 290 326 V294 Q290 288 296 288 Z" fill="var(--orange)"/>
    <text class="tagline" x="318" y="317">The Classic Kordo Bolt Products</text>
  </svg>

  <!-- Back of card -->
  <svg class="card card-back" viewBox="0 0 700 400" xmlns="http://www.w3.org/2000/svg">
    <rect width="700" height="400" fill="var(--card-white)"/>
    <path class="sweep-stripe" d="M0 92 H250 C390 118 540 175 700 198 V214 C540 192 390 136 240 106 H0 Z" fill="var(--orange)"/>
    <path class="header-band" d="M0 0 H700 V190 C540 166 390 110 250 86 H0 Z" fill="var(--charcoal)"/>
    <text class="brand-name" x="36" y="58">BRAMBLE GEAR</text>

    <g class="service-list">
      <path class="service-ribbon" d="M0 124 H300 L284 143 L300 162 H0 Z" fill="var(--orange)"/>
      <text class="service-label" x="28" y="150">Canvas Seat Covers</text>
      <path class="service-ribbon" d="M0 180 H270 L254 199 L270 218 H0 Z" fill="var(--orange)"/>
      <text class="service-label" x="28" y="206">Hi - Vis Flags</text>
      <path class="service-ribbon" d="M0 236 H300 L284 255 L300 274 H0 Z" fill="var(--orange)"/>
      <text class="service-label" x="28" y="262">Canvas or PVC designs</text>
    </g>

    <g class="contact-block">
      <text class="holder-name" x="395" y="256">Danielle Rowbeck</text>
      <line x1="380" y1="272" x2="680" y2="272" stroke="var(--ink)" stroke-width="1.2"/>

      <g class="contact-phone">
        <circle class="icon-ring" cx="398" cy="302" r="12"/>
        <path class="icon-glyph" d="M391 298 q7 -6 14 0 v3 h-3 v-2 h-8 v2 h-3 Z M393 302 h12 v7 h-12 Z"/>
        <text class="contact-line" x="422" y="308">02 49315728</text>
      </g>
      <g class="contact-email">
        <circle class="icon-ring" cx="398" cy="335" r="12"/>
        <rect class="icon-glyph" x="391" y="330" width="14" height="10" rx="1"/>
        <path d="M391 330 L398 336 L405 330" fill="none" stroke="var(--card-white)" stroke-width="1.4"/>
        <text class="contact-line" x="422" y="341">admin@bramblegear.com.au</text>
      </g>
      <g class="contact-web">
        <circle class="icon-ring" cx="398" cy="368" r="12"/>
        <rect x="391" y="362" width="14" height="9" rx="1" fill="none" stroke="var(--orange)" stroke-width="2"/>
        <rect class="icon-glyph" x="395" y="372" width="6" height="2"/>
        <text class="contact-line" x="422" y="374">www.bramblegear.com.au</text>
      </g>
    </g>
  </svg>

</main>
</body>
</html>
```